TWIG - Tiny Wild Infusion Garden - Craft Cocktails Mixes.

and we want to sell craft cocktails mixes (dried ingredients) in jars. The person buying them would add the alcohol.

LOGO TO BE WHITE ON WEBSITE

We are doing something similar to this, but would like to make them better... with better names and better mixers.

Here are some competing sites.

https://www.fernhollowmixers.com

https://pennyspours.com

In terms of style, I love this layout and look of a website:

https://www.rvdunespirits.com/

Or this

https://www.stitchthevale.com/

Target Market(s)

Target market is 21-50. Anyone who wants to throw a party or make amazing cocktails, but doesn't have the full bar to do so. It's just pour... wait 3 days. Strain. Mix with soda, tonic, fruit juice, kombucha over ice and drink.

Coding

Coded - Design and coding required

Number of Pages Required

5+ page

Other font styles liked:
• LOGO TO BE WHITE ON WEBSITE - Match the font of the Logo

Colors
00AB8E
00BBA5
67D7C9
C6EFE9
E9F9F6

Requirements
Must have
• Point of sale. The ability to add photos and videos with ease
Nice to have
• Great photography. Teal background tabs with white logo.

```html
<!DOCTYPE html>
<html lang="en">
<head>
<meta charset="utf-8">
<title>TWIG — Craft Cocktail Mixes</title>
<link href="https://fonts.googleapis.com/css2?family=Josefin+Sans:wght@300;400&family=Cormorant+Garamond:wght@300&family=Merriweather:wght@300;400&display=swap" rel="stylesheet">
<style>
:root{
  --teal:#007a78;
  --teal-link:#1a9a94;
  --ink:#2c2c2c;
  --muted:#666;
  --ghost:#e3e3e3;
  --lime:#d6df6c;
  --hero-link:#dfe38a;
  --white:#fff;
  --head:'Josefin Sans',sans-serif;
  --ghost-font:'Cormorant Garamond',serif;
  --body:'Merriweather',serif;
}
*{box-sizing:border-box;margin:0;padding:0}
html,body{width:1200px;height:4465px;overflow:hidden;background:var(--white)}
.page{position:relative;width:1200px;height:4465px;overflow:hidden;font-family:var(--body);color:var(--ink)}
.abs{position:absolute}
.photo{position:absolute}
.brand{position:absolute;text-align:center;font-family:var(--head);color:var(--ink);line-height:1}
.brand .name{font-size:46px;font-weight:400;letter-spacing:4px}
.brand .tag{font-size:9px;letter-spacing:1.5px;margin-top:6px;text-transform:uppercase}
.nav{position:absolute;top:48px;font-family:var(--body);font-size:14px;color:#444}
.nav.active{color:var(--teal-link);border-bottom:1px solid var(--teal-link);padding-bottom:4px}
.link{position:absolute;font-family:var(--body);font-size:11px;letter-spacing:2.5px;text-transform:uppercase;color:var(--teal-link);border-bottom:1px solid var(--teal-link);padding-bottom:3px;white-space:nowrap}
.link svg{vertical-align:middle;margin-left:8px}
.ghost{position:absolute;font-family:var(--ghost-font);font-weight:300;color:var(--ghost);line-height:1;white-space:nowrap}
.title{position:absolute;font-family:var(--head);font-weight:300;text-transform:uppercase;color:var(--ink);white-space:nowrap}
.copy{position:absolute;font-family:var(--body);font-weight:300;font-size:14px;line-height:23px;color:var(--muted)}
.product{position:absolute;width:200px;text-align:center}
.product .jar{width:150px;height:260px;margin:0 auto;border-radius:38px 38px 24px 24px}
.product .pname{font-size:15px;font-weight:300;letter-spacing:2px;margin-top:20px;color:#444}
.product .price{font-size:13px;font-weight:300;letter-spacing:2.5px;margin-top:9px;color:#444}
.special-title{position:absolute;font-family:var(--head);font-weight:300;font-size:25px;color:var(--ink)}
.foot-h{position:absolute;font-family:var(--ghost-font);font-size:22px;color:#444;text-align:center;width:260px}
.foot-t{position:absolute;font-size:13px;color:#555;text-align:center;width:260px;line-height:20px}
</style>
</head>
<body>
<div class="page">

  <header>
    <div class="brand" style="left:160px;top:24px;width:140px">
      <div class="name">TWIG</div>
      <div class="tag">Tiny Wild Infusion Garden</div>
    </div>
    <span class="nav active" style="left:467px">Home</span>
    <span class="nav" style="left:558px">Pages</span>
    <span class="nav" style="left:648px">Blog</span>
    <span class="nav" style="left:728px">Shop</span>
    <span class="nav" style="left:812px">Recipes</span>
    <span class="nav" style="left:915px">Search
      <svg width="14" height="14" viewBox="0 0 14 14" style="vertical-align:-2px;margin-left:4px"><circle cx="6" cy="6" r="4.2" fill="none" stroke="#333" stroke-width="2"/><line x1="9" y1="9" x2="13" y2="13" stroke="#333" stroke-width="2"/></svg>
    </span>
    <svg class="abs" style="left:1008px;top:44px" width="34" height="22" viewBox="0 0 34 22" aria-label="Cart">
      <path d="M2 6h18l-3 10H5z" fill="var(--teal-link)"/>
      <circle cx="27" cy="7" r="6" fill="var(--teal-link)"/>
      <text x="27" y="10" font-size="9" fill="#fff" text-anchor="middle" font-family="Merriweather,serif">0</text>
    </svg>
  </header>

  <section class="hero">
    <div class="photo" role="img" aria-label="Jars of dried cocktail ingredients beside martini glasses and a cocktail shaker" style="left:0;top:115px;width:1200px;height:480px;background:linear-gradient(180deg,#a9adaf 0%,#b9bcbd 72%,#d4d6d6 74%,#e2e3e2 100%)"></div>
    <div class="photo" role="img" aria-label="Glass jars with teal labels, filled with dried orange and berries" style="left:455px;top:240px;width:320px;height:330px;border-radius:40px 40px 20px 20px;background:radial-gradient(ellipse at 45% 65%,#e7a33a 0%,#c8873a 35%,rgba(190,190,190,.3) 75%,rgba(190,190,190,0) 100%)"></div>
    <div class="photo" role="img" aria-label="Martini glasses with olives and a gold shaker" style="left:700px;top:160px;width:500px;height:420px;background:radial-gradient(ellipse at 65% 40%,rgba(215,190,120,.55) 0%,rgba(200,200,190,.25) 50%,rgba(200,200,200,0) 80%)"></div>
    <div class="abs" style="left:160px;top:206px;color:#fff;font-family:var(--head);font-weight:300">
      <div style="font-size:22px">Enjoy some of the</div>
      <div style="font-size:40px;line-height:46px;margin-top:6px">Most Sell Craft<br>Cocktails Mixes</div>
      <div style="font-size:17px;margin-top:12px">(DRIED INGREDIENTS) IN JARS</div>
    </div>
    <span class="link" style="left:163px;top:399px;color:var(--hero-link);border-color:var(--hero-link);font-size:13px">Shop now
      <svg width="18" height="8" viewBox="0 0 18 8"><path d="M0 4h16M12 1l4 3-4 3" stroke="currentColor" fill="none"/></svg></span>
  </section>

  <section class="craft">
    <div class="ghost" style="left:142px;top:618px;font-size:140px">Craft</div>
    <div class="photo" role="img" aria-label="Tipped jar spilling dried citrus and mushrooms on a wooden table" style="left:160px;top:745px;width:318px;height:402px;background:linear-gradient(135deg,#7b4a2a 0%,#b36a35 45%,#8a5a3a 75%,#5a3a26 100%)"></div>
    <div class="title" style="left:488px;top:810px;width:224px;text-align:center;font-size:24px">Craft Cocktails</div>
    <div class="copy" style="left:500px;top:858px;width:200px;text-align:center;font-size:14px;line-height:22px">Lorem ipsum dolor sit amet, consteadipiscing consectetur adipiscing elit</div>
    <span class="link" style="left:550px;top:968px">View all
      <svg width="18" height="8" viewBox="0 0 18 8"><path d="M0 4h16M12 1l4 3-4 3" stroke="currentColor" fill="none"/></svg></span>
    <div class="photo" role="img" aria-label="Jar of dried grapefruit slices in a warm bar interior" style="left:723px;top:676px;width:318px;height:403px;background:radial-gradient(ellipse at 50% 65%,#d9824a 0%,#a5602f 35%,#5b3a22 75%,#3b2617 100%)"></div>
    <div class="ghost" style="left:712px;top:1072px;font-size:128px">Cocktails</div>
  </section>

  <section class="products">
    <div class="ghost" style="left:430px;top:1202px;font-size:106px">Products</div>
    <div class="title" style="left:466px;top:1252px;font-size:36px">Our Products</div>
    <div class="product" style="left:167px;top:1344px">
      <div class="jar" role="img" aria-label="Jar of dried orange slices" style="background:linear-gradient(180deg,#d9d9d6 0%,#c6843e 35%,#a0562a 75%,#7a4226 100%)"></div>
      <div class="pname">Lorem ipsum</div><div class="price">$ 26.00</div>
    </div>
    <div class="product" style="left:389px;top:1344px">
      <div class="jar" role="img" aria-label="Jar of dried apple and pear slices" style="background:linear-gradient(180deg,#dcdcd8 0%,#c9b982 35%,#9f8d58 75%,#6f6444 100%)"></div>
      <div class="pname">Lorem ipsum</div><div class="price">$ 26.00</div>
    </div>
    <div class="product" style="left:628px;top:1344px">
      <div class="jar" role="img" aria-label="Jar of dried pineapple pieces" style="background:linear-gradient(180deg,#dcdcd8 0%,#e0c37a 35%,#c4a159 75%,#8e7544 100%)"></div>
      <div class="pname">Lorem ipsum</div><div class="price">$ 26.00</div>
    </div>
    <div class="product" style="left:866px;top:1344px">
      <div class="jar" role="img" aria-label="Jar of dried lemon and lime slices" style="background:linear-gradient(180deg,#dcdcd8 0%,#e3d556 35%,#b9a236 75%,#7e6f2c 100%)"></div>
      <div class="pname">Lorem ipsum</div><div class="price">$ 26.00</div>
    </div>
    <span class="link" style="left:508px;top:1683px">View allproducts
      <svg width="18" height="8" viewBox="0 0 18 8"><path d="M0 4h16M12 1l4 3-4 3" stroke="currentColor" fill="none"/></svg></span>
  </section>

  <section class="recipes">
    <div class="ghost" style="left:396px;top:1766px;font-size:106px">Recipes</div>
    <div class="photo" role="img" aria-label="Jars of dried berries and fruit on a wooden board against a blue wall" style="left:593px;top:1862px;width:404px;height:479px;background:linear-gradient(180deg,#9fc8e2 0%,#a9cfe6 45%,#c05a58 62%,#8a5a3a 82%,#6d4630 100%)"></div>
    <div class="abs" style="left:203px;top:1888px;width:416px;height:477px;background:var(--teal)"></div>
    <div class="title" style="left:203px;top:1934px;width:416px;text-align:center;color:#fff;font-size:34px">Recipes</div>
    <div class="abs" style="left:423px;top:1990px;width:1px;height:178px;background:rgba(255,255,255,.35)"></div>
    <div class="copy" style="left:222px;top:2188px;width:380px;text-align:center;color:#fff;font-size:14px;line-height:25px">Lorem ipsum dolor sit amet, consectetur adipiscing elit. Integer sit amet rutrum lacus. Fusce pharetra ex sit amet lectus vehicula, ut convallis nisi laoreet.</div>
    <span class="link" style="left:338px;top:2293px;color:#fff;border-color:#fff">View all recipes
      <svg width="18" height="8" viewBox="0 0 18 8"><path d="M0 4h16M12 1l4 3-4 3" stroke="currentColor" fill="none"/></svg></span>
  </section>

  <section class="choose">
    <div class="photo" role="img" aria-label="Sketched margarita glass and mason jar mug with lime" style="left:173px;top:2436px;width:356px;height:304px;background:radial-gradient(ellipse at 50% 55%,#e4e07a 0%,#d4d08a 35%,#eeeed8 70%,#ffffff 100%)"></div>
    <div class="photo" role="img" aria-label="Faint cocktail glass decoration" style="left:950px;top:2406px;width:250px;height:342px;background:radial-gradient(ellipse at 50% 45%,#f0f0f0 0%,#f6f6f6 55%,rgba(255,255,255,0) 80%)"></div>
    <div class="ghost" style="left:593px;top:2430px;font-size:112px">Choose</div>
    <div class="title" style="left:603px;top:2530px;font-size:35px">Choose your cocktail</div>
    <div class="copy" style="left:605px;top:2593px;width:440px;font-size:14px;line-height:25px">Lorem ipsum dolor sit amet, consectetur adipising elit. Integer sit amet rutrum lacus. Fusce pharetra ex sit aet lectus vehicula, ut convallis nisi laoreet.</div>
    <span class="link" style="left:605px;top:2695px">Shop cocktails
      <svg width="18" height="8" viewBox="0 0 18 8"><path d="M0 4h16M12 1l4 3-4 3" stroke="currentColor" fill="none"/></svg></span>
  </section>

  <section class="specials">
    <div class="ghost" style="left:442px;top:2806px;font-size:106px">Specials</div>
    <div class="title" style="left:522px;top:2842px;font-size:36px">Specials</div>

    <div class="photo" role="img" aria-label="Jar tipped over with dried apple rings and twigs" style="left:160px;top:2913px;width:312px;height:226px;background:linear-gradient(180deg,#dcdcdc 0%,#cfcfcf 50%,#c99a5c 72%,#3c3432 100%)"></div>
    <div class="special-title" style="left:160px;top:3150px">Lorem ipsum dolor</div>
    <div class="copy" style="left:160px;top:3186px;width:300px;font-size:14px;line-height:22px">Lorem ipsum dolor sit amet, consectetur adipiscing elit. Integer</div>
    <span class="link" style="left:160px;top:3242px">Know more
      <svg width="18" height="8" viewBox="0 0 18 8"><path d="M0 4h16M12 1l4 3-4 3" stroke="currentColor" fill="none"/></svg></span>

    <div class="photo" role="img" aria-label="Close-up of dried fruit ribbons in a jar" style="left:498px;top:2957px;width:204px;height:225px;background:radial-gradient(ellipse at 50% 50%,#f2d27a 0%,#d8a84a 45%,#7a5a2a 100%)"></div>
    <div class="special-title" style="left:498px;top:3197px">Lorem ipsum</div>
    <div class="copy" style="left:498px;top:3235px;width:210px;font-size:14px;line-height:22px">Lorem ipsum dolor sit amet, consectetur adipiscing elit. Integer</div>
    <span class="link" style="left:498px;top:3309px">Know more
      <svg width="18" height="8" viewBox="0 0 18 8"><path d="M0 4h16M12 1l4 3-4 3" stroke="currentColor" fill="none"/></svg></span>

    <div class="photo" role="img" aria-label="Row of three mixer jars under bar lights" style="left:728px;top:2913px;width:312px;height:226px;background:linear-gradient(180deg,#6a3a2a 0%,#5a5aa0 40%,#7fb6c8 62%,#b58a4a 82%,#4a3a3a 100%)"></div>
    <div class="special-title" style="left:728px;top:3150px">Lorem ipsum dolor</div>
    <div class="copy" style="left:728px;top:3186px;width:300px;font-size:14px;line-height:22px">Lorem ipsum dolor sit amet, consectetur adipiscing elit. Integer</div>
    <span class="link" style="left:728px;top:3242px">Know more
      <svg width="18" height="8" viewBox="0 0 18 8"><path d="M0 4h16M12 1l4 3-4 3" stroke="currentColor" fill="none"/></svg></span>
  </section>

  <section class="feed">
    <div class="title" style="left:0;width:1200px;text-align:center;top:3410px;font-size:32px">Follow Our Feed</div>
    <div class="photo" role="img" aria-label="Jar of dried strawberries from above" style="left:35px;top:3478px;width:253px;height:255px;background:radial-gradient(circle at 50% 55%,#a8343a 0%,#8a3a3a 40%,#c9c9c6 75%,#dedede 100%)"></div>
    <div class="photo" role="img" aria-label="Labelled jar on a dark background" style="left:326px;top:3517px;width:255px;height:254px;background:radial-gradient(ellipse at 50% 55%,#87b9c4 0%,#4a3034 45%,#1b1414 100%)"></div>
    <div class="photo" role="img" aria-label="Jar with dried flowers and twine" style="left:619px;top:3478px;width:255px;height:255px;background:radial-gradient(ellipse at 50% 55%,#c9a070 0%,#8a7a6a 45%,#5a5452 100%)"></div>
    <div class="photo" role="img" aria-label="Cocktail glasses and a jar of dried fruit in warm light" style="left:912px;top:3517px;width:255px;height:254px;background:radial-gradient(ellipse at 60% 45%,#d7955a 0%,#8a4e2a 45%,#2e1c14 100%)"></div>
  </section>

  <section class="newsletter">
    <div class="abs" style="left:0;top:3857px;width:1200px;height:235px;background:var(--teal)"></div>
    <div class="abs" style="left:0;width:1200px;top:3894px;text-align:center;color:#fff;font-size:11px;letter-spacing:5px">SUBSCRIBE</div>
    <div class="title" style="left:0;width:1200px;text-align:center;top:3916px;font-size:36px;color:#fff">Newsletter for latest update</div>
    <div class="abs" style="left:291px;top:3981px;width:441px;height:53px;background:#fff;font-size:13px;color:#666;padding:18px 20px">Email Address</div>
    <div class="abs" style="left:746px;top:3981px;width:163px;height:53px;background:var(--lime);font-family:var(--body);font-size:16px;color:#555;text-align:center;line-height:53px">Subscribe</div>
  </section>

  <footer>
    <div class="foot-h" style="left:155px;top:4176px">Contact Us</div>
    <div class="foot-t" style="left:155px;top:4225px">18 Larkspur Row, Millbrook,<br>NY 12545, USA</div>
    <div class="foot-t" style="left:155px;top:4283px">+1 555 014 2087</div>
    <div class="foot-t" style="left:155px;top:4319px">+1 555 019 3364</div>
    <svg class="abs" style="left:237px;top:4364px" width="96" height="14" viewBox="0 0 96 14" aria-label="Social links">
      <circle cx="6" cy="7" r="5" fill="#222"/><circle cx="44" cy="7" r="5" fill="#222"/><circle cx="86" cy="7" r="5" fill="#222"/>
    </svg>

    <div class="brand" style="left:500px;top:4160px;width:200px">
      <div class="name" style="font-size:58px">TWIG</div>
      <div class="tag" style="font-size:10px">Tiny Wild Infusion Garden</div>
    </div>
    <div class="foot-t" style="left:440px;top:4284px;width:320px">Lorem ipsum dolor sit amet, conser adipiscing elit, sed do eiusmod tempor incididunt ut</div>
    <svg class="abs" style="left:501px;top:4344px" width="198" height="18" viewBox="0 0 198 18" aria-label="Accepted payment methods">
      <rect x="0" y="1" width="30" height="16" rx="2" fill="#1f2d4a"/>
      <rect x="42" y="1" width="30" height="16" rx="2" fill="#1f2d4a"/>
      <rect x="84" y="1" width="30" height="16" rx="2" fill="#1f2d4a"/>
      <rect x="126" y="1" width="30" height="16" rx="2" fill="#1f2d4a"/>
      <rect x="168" y="1" width="30" height="16" rx="2" fill="#1f2d4a"/>
    </svg>

    <div class="foot-h" style="left:775px;top:4176px">Working Hours</div>
    <div class="foot-t" style="left:775px;top:4226px">Monday-Friday</div>
    <div class="foot-t" style="left:775px;top:4258px">08:00-22:00</div>
    <div class="foot-t" style="left:775px;top:4290px">Saturday-Sunday</div>
    <div class="foot-t" style="left:775px;top:4322px">10:00-16:00</div>

    <div class="abs" style="left:0;width:1200px;top:4430px;text-align:center;font-size:12px;color:#666">© 2021 <span style="color:#222">TWIG</span>. All right reserved.</div>
    <div class="abs" style="left:1024px;top:4432px;transform:rotate(-90deg);transform-origin:left top;font-size:11px;letter-spacing:1px;color:var(--teal-link);border-bottom:1px solid var(--teal-link)">TOP</div>
  </footer>

</div>
</body>
</html>
```